Electrician Company Website Design

I am looking to get a website designed only. I do not need it converted ot html. I simply need the design in a psd format. I have my own team for the conversion. The website is for an electrician company called Bramblecourt electric. I have created a txt document with the project parameters and specifics. I have also uploaded their logo in all avaible formats. It's a zip file.

Number of Pages Required

1 page

```html
<!DOCTYPE html>
<html lang="en">
<head>
<meta charset="utf-8">
<title>Bramblecourt Electric</title>
<link href="https://fonts.googleapis.com/css2?family=Roboto:wght@400;500;700&family=Raleway:wght@400;500;600&display=swap" rel="stylesheet">
<style>
:root{
  --blue:#1f5fb4;
  --blue-dark:#174c93;
  --red:#a3292c;
  --red-dark:#8f2225;
  --ink:#161616;
  --text:#555;
  --light:#f2f2f2;
  --white:#fff;
}
*{margin:0;padding:0;box-sizing:border-box}
html,body{width:1200px;height:4882px;overflow:hidden}
body{position:relative;background:var(--white);font-family:"Raleway",sans-serif;color:var(--ink)}
.abs{position:absolute}
h2.section-title{font-family:"Roboto",sans-serif;font-weight:500;font-size:34px;letter-spacing:.5px;text-transform:uppercase}
.title-rule{position:absolute;height:3px;width:100px;background:var(--blue)}
.btn{position:absolute;display:flex;align-items:center;justify-content:center;font-family:"Roboto",sans-serif;font-weight:500;font-size:14px;color:var(--white)}
.btn.red{background:var(--red)}
.btn.blue{background:var(--blue)}
.body-copy{font-size:14px;line-height:24px;color:var(--text)}

/* header */
.site-header{position:absolute;left:0;top:0;width:1200px;height:80px;background:var(--white)}
.brand{position:absolute;left:108px;top:28px;display:flex;align-items:center;gap:8px;font-family:"Roboto",sans-serif;font-weight:700;font-size:15px;color:var(--ink)}
.brand .dot{width:14px;height:14px;border-radius:50%;background:var(--blue)}
.topbar{position:absolute;left:872px;top:0;width:228px;height:25px;background:var(--blue);color:var(--white);font-family:"Roboto",sans-serif;font-size:10px;display:flex;align-items:center;justify-content:center;gap:8px}
.main-nav a{position:absolute;top:40px;font-family:"Roboto",sans-serif;font-size:10.5px;font-weight:500;color:var(--ink);text-decoration:none}
.main-nav a.active{color:var(--red)}

/* hero */
.hero{position:absolute;left:0;top:80px;width:1200px;height:612px}
.hero-kicker{position:absolute;left:100px;top:128px;color:var(--white);font-size:21px;letter-spacing:4px;font-weight:500}
.hero-title{position:absolute;left:100px;top:160px;color:var(--white);font-family:"Roboto",sans-serif;font-weight:700;font-size:58px;line-height:71px}

/* about */
.about-photo{position:absolute;left:80px;top:777px;width:430px;height:455px}
.about-title{position:absolute;left:607px;top:818px}
.about-copy{position:absolute;left:607px;top:898px;width:505px}

/* services */
.services{position:absolute;left:0;top:1323px;width:1200px;height:639px;background:linear-gradient(135deg,#2a6cc0,#1a56a6 60%,#2364b6)}
.card{position:absolute;top:162px;width:321px;height:415px;background:var(--white);text-align:center}
.card .photo{height:187px}
.card h3{margin-top:30px;font-family:"Roboto",sans-serif;font-weight:500;font-size:13px;text-transform:uppercase}
.card p{margin:16px auto 0;width:275px;font-size:10.5px;line-height:18px;color:var(--text)}
.card .outline{position:absolute;left:82px;top:346px;width:157px;height:37px;border:1px solid var(--red);color:var(--red);font-family:"Roboto",sans-serif;font-weight:500;font-size:14px;display:flex;align-items:center;justify-content:center}

/* areas */
.area-item{position:absolute;display:flex;align-items:center;gap:12px;font-family:"Roboto",sans-serif;font-size:13px}
.pin{width:18px;height:18px;border-radius:50%;border:1px solid #e9a3a4;display:flex;align-items:center;justify-content:center}

/* gallery */
.gallery{position:absolute;left:0;top:2480px;width:1200px;height:625px;background:linear-gradient(135deg,#a8302f,#8e2326)}
.gallery .tile{position:absolute}

/* faq */
.faq-item{position:absolute;height:57px;background:var(--light);display:flex;align-items:center;justify-content:space-between;padding:0 14px 0 12px;font-family:"Roboto",sans-serif;font-weight:500;font-size:13px}
.faq-item .sign{font-size:20px;font-weight:400;color:#666}
.faq-open{position:absolute;left:100px;top:3308px;width:494px}
.faq-open .head{background:var(--red);color:var(--white);font-family:"Roboto",sans-serif;font-weight:500;font-size:13px;line-height:30px;padding:14px 12px;position:relative;height:86px}
.faq-open .head .sign{position:absolute;right:16px;top:14px;font-size:18px}
.faq-open .body{background:var(--light);padding:14px 12px;font-size:10px;line-height:18px;color:var(--text);height:104px}

/* contact */
.field-label{position:absolute;font-size:14px;font-weight:500;letter-spacing:1px}
.field{position:absolute;height:37px;background:var(--light);font-size:9px;color:#999;padding:0 12px;display:flex;align-items:center}
.field.focus{background:var(--white);border:1px solid #8aa6c8}

/* footer */
.footer{position:absolute;left:0;top:4400px;width:1200px;height:482px}
.footer-brand{position:absolute;left:0;top:4405px;width:1200px;display:flex;justify-content:center;align-items:center;gap:10px;font-family:"Roboto",sans-serif;font-weight:700;font-size:22px;color:var(--white)}
.footer-brand .dot{width:18px;height:18px;border-radius:50%;background:var(--white)}
.footer h4{position:absolute;top:4548px;color:var(--white);font-family:"Roboto",sans-serif;font-weight:500;font-size:21px}
.foot-link{position:absolute;left:100px;color:#dbe6f5;font-size:13.5px}
.contact-row{position:absolute;left:336px;display:flex;align-items:center;gap:22px;color:#dbe6f5;font-size:13.5px}
.contact-row .ic{width:27px;height:27px;border-radius:50%;background:var(--white);display:flex;align-items:center;justify-content:center}
.social{position:absolute;top:4770px;width:24px;height:24px;border-radius:50%;background:var(--white);display:flex;align-items:center;justify-content:center}
.social span{width:10px;height:10px;background:var(--red);border-radius:2px}
</style>
</head>
<body>

<header class="site-header">
  <div class="brand"><span class="dot"></span>Bramblecourt Electric</div>
  <div class="topbar">
    <svg width="11" height="11" viewBox="0 0 24 24"><path d="M6.6 10.8a15 15 0 0 0 6.6 6.6l2.2-2.2a1 1 0 0 1 1-.25 11.4 11.4 0 0 0 3.6.57 1 1 0 0 1 1 1V20a1 1 0 0 1-1 1A17 17 0 0 1 3 4a1 1 0 0 1 1-1h3.5a1 1 0 0 1 1 1c0 1.25.2 2.45.57 3.57a1 1 0 0 1-.25 1z" fill="#fff"/></svg>
    Contact Us On 555 014 2297
  </div>
  <nav class="main-nav">
    <a class="active" style="left:550px">Home</a>
    <a style="left:608px">About Company</a>
    <a style="left:715px">Our Services</a>
    <a style="left:813px">Service Areas</a>
    <a style="left:908px">Our Gallery</a>
    <a style="left:990px">FAQ's</a>
    <a style="left:1043px">Contact Us</a>
  </nav>
</header>

<section class="hero">
  <svg width="1200" height="612" viewBox="0 0 1200 612" style="position:absolute;left:0;top:0">
    <defs>
      <radialGradient id="bulbGlow" cx="0.62" cy="0.45" r="0.5">
        <stop offset="0" stop-color="#f6a531"/>
        <stop offset="0.35" stop-color="#a8511a"/>
        <stop offset="1" stop-color="#0b0b0b"/>
      </radialGradient>
    </defs>
    <rect width="1200" height="612" fill="#0b0b0b"/>
    <rect x="625" y="0" width="575" height="500" fill="url(#bulbGlow)" role="img" aria-label="Glowing filament light bulb hanging in the dark"/>
    <path d="M0,470 C50,540 200,548 380,552 L600,612 L820,552 C1000,548 1150,540 1200,470 L1200,612 L0,612Z" fill="var(--blue)"/>
    <path d="M0,548 C60,605 220,600 400,604 L600,612 L800,604 C980,600 1140,605 1200,548 L1200,612 L0,612Z" fill="#fff"/>
  </svg>
  <div class="hero-kicker">WE ARE BRAMBLECOURT ELECTRIC</div>
  <h1 class="hero-title">FAST ELECTRICAL<br>SERVICE PROVIDER</h1>
  <div class="btn red" style="left:100px;top:348px;width:160px;height:37px">Contact Us</div>
  <div class="btn blue" style="left:277px;top:348px;width:155px;height:37px">Our Services</div>
</section>

<section class="about">
  <svg class="about-photo" viewBox="0 0 430 455" role="img" aria-label="Electrician in blue overalls and yellow helmet holding tools">
    <circle cx="215" cy="240" r="212" fill="#e4e4e4"/>
    <circle cx="215" cy="240" r="205" fill="none" stroke="var(--blue)" stroke-width="12" stroke-dasharray="0 330 660"/>
    <circle cx="215" cy="240" r="200" fill="#d8dee6"/>
  </svg>
  <h2 class="section-title about-title">About Us</h2>
  <p class="body-copy about-copy">Lorem ipsum dolor sit amet consectetur. Ultricies id curabitur commodo amet enim elementum gravida. Commodo semper vestibulum in nisl sed. At dolor ac neque ipsum purus auctor sem sem. Netus velit posuere sit varius gravida consequat euismod arcu purus. Tincidunt vivamus odio egestas nulla elementum non a nibh. Vitae volutpat nulla scelerisque adipiscing amet at egestas. Elementum quisque amet scelerisque id non pharetra integer purus quam. Viverra quis amet sed et scelerisque egestas semper lectus. Amet aliquam et volutpat dignissim morbi turpis elementum est sed.</p>
  <div class="btn red" style="left:607px;top:1162px;width:155px;height:36px">Read More</div>
</section>

<section class="services">
  <h2 class="section-title" style="position:absolute;left:0;width:1200px;top:62px;text-align:center;color:#fff">Our Services</h2>
  <div class="title-rule" style="left:550px;top:108px;background:#fff"></div>

  <div class="card" style="left:100px">
    <div class="photo" role="img" aria-label="Lineman working on a power pole" style="background:linear-gradient(160deg,#7f93ad,#3e4f66)"></div>
    <h3>Commerical Electrical Services</h3>
    <p>Lorem ipsum dolor sit amet consectetur. Ultricies id curabitur commodo amet enim elementum gravida. Commodo semper vestibulum in nisl sed. At dolor ac neque ipsum purus auctor sem sem. Netus velit</p>
    <div class="outline">Read More</div>
  </div>
  <div class="card" style="left:440px">
    <div class="photo" role="img" aria-label="Lit modern house among trees at dusk" style="background:linear-gradient(160deg,#3a4540,#151a1a)"></div>
    <h3>Residential Electrical Services</h3>
    <p>Lorem ipsum dolor sit amet consectetur. Ultricies id curabitur commodo amet enim elementum gravida. Commodo semper vestibulum in nisl sed. At dolor ac neque ipsum purus auctor sem sem. Netus velit</p>
    <div class="outline">Read More</div>
  </div>
  <div class="card" style="left:779px">
    <div class="photo" role="img" aria-label="Electrician in hard hat wiring a panel" style="background:linear-gradient(160deg,#8a7b66,#4a4036)"></div>
    <h3>Industrial Electrical Services</h3>
    <p>Lorem ipsum dolor sit amet consectetur. Ultricies id curabitur commodo amet enim elementum gravida. Commodo semper vestibulum in nisl sed. At dolor ac neque ipsum purus auctor sem sem. Netus velit</p>
    <div class="outline">Read More</div>
  </div>
</section>

<section class="areas">
  <h2 class="section-title" style="position:absolute;left:100px;top:2056px">Service Areas</h2>
  <p class="body-copy" style="position:absolute;left:100px;top:2134px;width:510px">Lorem ipsum dolor sit amet consectetur. Ultricies id curabitur commodo amet enim elementum gravida. Commodo semper vestibulum in nisl sed. At dolor ac neque ipsum purus auctor sem sem. Netus velit posuere</p>

  <div class="area-item" style="left:100px;top:2236px"><span class="pin"><svg width="8" height="10" viewBox="0 0 8 10"><path d="M4 0a3.5 3.5 0 0 0-3.5 3.5C.5 6 4 10 4 10s3.5-4 3.5-6.5A3.5 3.5 0 0 0 4 0z" fill="var(--red)"/></svg></span>LARKMOOR MN</div>
  <div class="area-item" style="left:277px;top:2236px"><span class="pin"><svg width="8" height="10" viewBox="0 0 8 10"><path d="M4 0a3.5 3.5 0 0 0-3.5 3.5C.5 6 4 10 4 10s3.5-4 3.5-6.5A3.5 3.5 0 0 0 4 0z" fill="var(--red)"/></svg></span>LARKMOOR MN</div>
  <div class="area-item" style="left:449px;top:2236px"><span class="pin"><svg width="8" height="10" viewBox="0 0 8 10"><path d="M4 0a3.5 3.5 0 0 0-3.5 3.5C.5 6 4 10 4 10s3.5-4 3.5-6.5A3.5 3.5 0 0 0 4 0z" fill="var(--red)"/></svg></span>LARKMOOR MN</div>
  <div class="area-item" style="left:100px;top:2274px"><span class="pin"><svg width="8" height="10" viewBox="0 0 8 10"><path d="M4 0a3.5 3.5 0 0 0-3.5 3.5C.5 6 4 10 4 10s3.5-4 3.5-6.5A3.5 3.5 0 0 0 4 0z" fill="var(--red)"/></svg></span>LARKMOOR MN</div>
  <div class="area-item" style="left:277px;top:2274px"><span class="pin"><svg width="8" height="10" viewBox="0 0 8 10"><path d="M4 0a3.5 3.5 0 0 0-3.5 3.5C.5 6 4 10 4 10s3.5-4 3.5-6.5A3.5 3.5 0 0 0 4 0z" fill="var(--red)"/></svg></span>LARKMOOR MN</div>
  <div class="area-item" style="left:449px;top:2274px"><span class="pin"><svg width="8" height="10" viewBox="0 0 8 10"><path d="M4 0a3.5 3.5 0 0 0-3.5 3.5C.5 6 4 10 4 10s3.5-4 3.5-6.5A3.5 3.5 0 0 0 4 0z" fill="var(--red)"/></svg></span>LARKMOOR MN</div>

  <div class="btn blue" style="left:100px;top:2345px;width:157px;height:36px">Read More</div>

  <div class="abs" style="left:730px;top:2148px;width:370px;height:238px;background:var(--blue)"></div>
  <div class="abs" role="img" aria-label="Electrician in white helmet and safety glasses working on a switchboard" style="left:711px;top:2057px;width:375px;height:317px;background:linear-gradient(135deg,#2c2f35,#6d7178 70%,#9aa0a6)"></div>
</section>

<section class="gallery">
  <h2 class="section-title" style="position:absolute;left:0;width:1200px;top:62px;text-align:center;color:#fff">Our Gallery</h2>
  <div class="title-rule" style="left:550px;top:108px;background:#fff"></div>
  <div class="tile" role="img" aria-label="Electrician at an outdoor meter box" style="left:100px;top:159px;width:306px;height:404px;background:linear-gradient(160deg,#5b4438,#3a2b24)"></div>
  <div class="tile" role="img" aria-label="Technician installing solar panels" style="left:417px;top:159px;width:321px;height:194px;background:linear-gradient(160deg,#6f96c2,#2f5b8f)"></div>
  <div class="tile" role="img" aria-label="Electrician inspecting a wiring cabinet" style="left:747px;top:159px;width:353px;height:194px;background:linear-gradient(160deg,#2b2d31,#8c9096)"></div>
  <div class="tile" role="img" aria-label="Hands holding coloured cables" style="left:417px;top:362px;width:199px;height:201px;background:linear-gradient(160deg,#3558a0,#c9a14a)"></div>
  <div class="tile" role="img" aria-label="Electrician working on a fuse board" style="left:626px;top:362px;width:265px;height:201px;background:linear-gradient(160deg,#2c2e33,#7d8289)"></div>
  <div class="tile" role="img" aria-label="Electrician checking circuit breakers" style="left:901px;top:362px;width:199px;height:201px;background:linear-gradient(160deg,#c9cbcf,#5a5e64)"></div>
</section>

<section class="faq">
  <h2 class="section-title" style="position:absolute;left:0;width:1200px;top:3198px;text-align:center">Frequently Asked Question</h2>
  <div class="title-rule" style="left:550px;top:3243px"></div>

  <div class="faq-open">
    <div class="head">Lorem ipsum dolor sit amet, consectetur adipiscing elit.<br>Non nibh ultrices volutpat ullamcorper ?<span class="sign">—</span></div>
    <div class="body">Lorem ipsum dolor sit amet, consectetur adipiscing elit. Tempor scelerisque tempor sollicitudin imperdiet. At integer sed quam nunc, risus pretium, ligula quis tellus. Tempor tincidunt porttitor nunc nascetur elementum mauris tortor eu, sit. Vulputate mauris porttitor eget eget volutpat, mauris morbi.</div>
  </div>
  <div class="faq-item" style="left:100px;top:3512px;width:494px">Lorem ipsum dolor sit amet, consectetur adipiscing elit.<span class="sign">+</span></div>
  <div class="faq-item" style="left:100px;top:3579px;width:494px">Lorem ipsum dolor sit amet, consectetur adipiscing elit.<span class="sign">+</span></div>
  <div class="faq-item" style="left:608px;top:3308px;width:492px">Lorem ipsum dolor sit amet, consectetur adipiscing elit.<span class="sign">+</span></div>
  <div class="faq-item" style="left:608px;top:3376px;width:492px">Lorem ipsum dolor sit amet, consectetur adipiscing elit.<span class="sign">+</span></div>
  <div class="faq-item" style="left:608px;top:3444px;width:492px">Lorem ipsum dolor sit amet, consectetur adipiscing elit.<span class="sign">+</span></div>
  <div class="faq-item" style="left:608px;top:3512px;width:492px">Lorem ipsum dolor sit amet, consectetur adipiscing elit.<span class="sign">+</span></div>
  <div class="faq-item" style="left:608px;top:3579px;width:492px">Lorem ipsum dolor sit amet, consectetur adipiscing elit.<span class="sign">+</span></div>

  <div class="btn blue" style="left:523px;top:3686px;width:156px;height:35px">Read All</div>
</section>

<section class="contact">
  <h2 class="section-title" style="position:absolute;left:100px;top:3814px">Get In Touch</h2>
  <div class="title-rule" style="left:100px;top:3859px"></div>

  <div class="field-label" style="left:100px;top:3896px">First Name:</div>
  <div class="field focus" style="left:100px;top:3923px;width:251px">|</div>
  <div class="field-label" style="left:383px;top:3896px">Last Name:</div>
  <div class="field" style="left:383px;top:3923px;width:250px">Write Here</div>

  <div class="field-label" style="left:100px;top:3983px">Phone Number:</div>
  <div class="field" style="left:100px;top:4010px;width:251px">Write Here</div>
  <div class="field-label" style="left:383px;top:3983px">Email:</div>
  <div class="field" style="left:383px;top:4010px;width:250px">Write Here</div>

  <div class="field-label" style="left:100px;top:4068px">Message:</div>
  <div class="field" style="left:100px;top:4095px;width:533px;height:76px;align-items:flex-start;padding-top:10px">Write Here</div>

  <div class="btn red" style="left:100px;top:4222px;width:158px;height:34px">Send</div>

  <div class="abs" style="left:730px;top:3938px;width:370px;height:318px;background:var(--blue)"></div>
  <div class="abs" role="img" aria-label="Worker in yellow helmet installing solar panel wiring on a rooftop" style="left:711px;top:3815px;width:375px;height:426px;background:linear-gradient(160deg,#dfe3e6,#9aa3a8 60%,#c9ced1)"></div>
</section>

<footer class="footer-wrap">
  <svg class="footer" width="1200" height="482" viewBox="0 0 1200 482">
    <path d="M0,75 Q600,-10 1200,75 L1200,482 L0,482Z" fill="var(--red)"/>
    <path d="M0,125 Q10,82 110,78 Q600,62 1090,78 Q1190,82 1200,125 L1200,482 L0,482Z" fill="var(--blue)"/>
  </svg>
  <div class="footer-brand" style="top:4464px"><span class="dot"></span>Bramblecourt Electric</div>

  <h4 style="left:100px">Quick Links</h4>
  <div class="foot-link" style="top:4594px">Home</div>
  <div class="foot-link" style="top:4624px">About Us</div>
  <div class="foot-link" style="top:4654px">Our Services</div>
  <div class="foot-link" style="top:4684px">Service Areas</div>
  <div class="foot-link" style="top:4714px">Our Gallery</div>
  <div class="foot-link" style="top:4744px">FAQ's</div>
  <div class="foot-link" style="top:4774px">Contact Us</div>

  <h4 style="left:336px">Contact Info</h4>
  <div class="contact-row" style="top:4595px"><span class="ic"><svg width="13" height="13" viewBox="0 0 24 24"><path d="M6.6 10.8a15 15 0 0 0 6.6 6.6l2.2-2.2a1 1 0 0 1 1-.25 11.4 11.4 0 0 0 3.6.57 1 1 0 0 1 1 1V20a1 1 0 0 1-1 1A17 17 0 0 1 3 4a1 1 0 0 1 1-1h3.5a1 1 0 0 1 1 1c0 1.25.2 2.45.57 3.57a1 1 0 0 1-.25 1z" fill="var(--blue)"/></svg></span>555 014 2297</div>
  <div class="contact-row" style="top:4638px"><span class="ic"><svg width="11" height="14" viewBox="0 0 8 10"><path d="M4 0a3.5 3.5 0 0 0-3.5 3.5C.5 6 4 10 4 10s3.5-4 3.5-6.5A3.5 3.5 0 0 0 4 0zm0 5a1.4 1.4 0 1 1 0-2.8A1.4 1.4 0 0 1 4 5z" fill="var(--red)"/></svg></span>12 Fenwick Row, Larkmoor</div>
  <div class="contact-row" style="top:4682px"><span class="ic"><svg width="13" height="10" viewBox="0 0 14 10"><rect x=".5" y=".5" width="13" height="9" rx="1" fill="none" stroke="var(--blue)"/><path d="M.5 .8 7 5.5 13.5 .8" fill="none" stroke="var(--blue)"/></svg></span>hello@bramblecourt.example</div>

  <h4 style="left:686px">Newsletter</h4>
  <p class="abs" style="left:686px;top:4598px;width:360px;color:#dbe6f5;font-size:13.5px;line-height:24px">Contact us using this form. A representative will answer your question as soon as possible</p>
  <div class="abs" style="left:686px;top:4673px;width:334px;height:61px;background:#fff;font-size:11px;display:flex;align-items:center;padding-left:24px">Email</div>
  <div class="abs" style="left:1020px;top:4673px;width:80px;height:61px;background:var(--red);display:flex;align-items:center;justify-content:center">
    <svg width="22" height="22" viewBox="0 0 24 24"><path d="M22 2 11 13M22 2l-7 20-4-9-9-4z" fill="none" stroke="#fff" stroke-width="1.6" stroke-linejoin="round"/></svg>
  </div>
  <div class="social" style="left:690px"><span></span></div>
  <div class="social" style="left:740px"><span></span></div>
  <div class="social" style="left:790px"><span></span></div>

  <div class="abs" style="left:0;top:4853px;width:1200px;text-align:center;color:#fff;font-size:13px;font-weight:500">Bramblecourt Electric ©2022</div>
</footer>

</body>
</html>
```